Full Service Outdoor Property Management Company

We are looking for a new and fresh business card design. My company has been in business for 26 years. Winter: We are a large snow and ice management company that does work for commercial, industrial and municipal clients. We have been named "Top 100 Snow Companies in the U.S." for numerous years. Summer: We provide complete landscape maintenance and landscape design and construction for both residential and commercial clients. We must incorporate our logo into card design as well as (in no particular order):
Employees name
Office: (417) 803-2765
Cell: (xxx) xxx-xxxx
brightfold.com
1879 Marigold, Dunmore MI 48276
(Something about 26 + years in business as well as "Top 100 snow contractors as stated above)
Target Market(s)
Winter: Commercial, Industrial, Municipal
Summer: Residential and Commercial
Industry/Entity Type
Construction
Contact Information for Business Card
This is a little challenging as we are using one card for essentially two companies that target different customers from summer to winter. Perhaps the back side could be split in two or something to highlight the different services?? I'm open to any ideas!! Looking forward to seeing what you come up with!
Requirements
Must have
- Logo
- (in no particular order)
- Employees name
- Office: (417) 803-2765
- Cell: (xxx) xxx-xxxx
- brightfold.com
- 1879 Marigold, Dunmore MI 48276
Nice to have
- Something about 26 + years in business
- "Top 100 Snow Contractors in the U.S."
Should not have
- Cheesy pictures of lawn mowers and snow plows

```html
<!DOCTYPE html>
<html lang="en">
<head>
<meta charset="utf-8">
<title>Brightfold Business Card</title>
<link href="https://fonts.googleapis.com/css2?family=Source+Sans+3:wght@400;600;700&display=swap" rel="stylesheet">
<style>
  :root {
    --page: #eceae6;
    --card-white: #ffffff;
    --brand-green: #2f8a45;
    --brand-green-dark: #226b33;
    --brand-blue: #1f7fd1;
    --brand-blue-light: #4aa3e8;
    --ink: #3a3a3a;
    --on-green: #ffffff;
    --shadow: rgba(0,0,0,0.18);
  }
  * { margin: 0; padding: 0; box-sizing: border-box; }
  html, body {
    width: 1200px; height: 720px; overflow: hidden;
    background: var(--page);
    font-family: "Source Sans 3", Arial, sans-serif;
  }
  .stage {
    width: 1200px; height: 720px;
    display: flex; align-items: center; justify-content: center; gap: 40px;
  }
  .card {
    position: relative;
    width: 540px; height: 309px;
    overflow: hidden;
    box-shadow: 0 6px 18px var(--shadow);
  }

  /* Front */
  .card-front { background: var(--card-white); color: var(--ink); }
  .card-front .waves { position: absolute; inset: 0; }
  .brand {
    position: absolute; left: 36px; top: 78px;
    display: flex; align-items: center; gap: 10px;
  }
  .brand-dot {
    width: 18px; height: 18px; border-radius: 50%;
    background: var(--brand-green);
  }
  .brand-name {
    font-size: 40px; font-weight: 700; color: var(--brand-green);
    letter-spacing: 0.5px;
  }
  .contact {
    position: absolute; left: 300px; top: 26px;
    list-style: none; font-size: 13px; line-height: 20px;
  }
  .contact li { display: flex; align-items: center; gap: 8px; }
  .contact svg { width: 13px; height: 13px; flex: none; }
  .contact .address { margin-top: 6px; padding-left: 21px; }
  .person {
    position: absolute; left: 36px; top: 232px; color: var(--on-green);
  }
  .person-name { font-size: 22px; font-weight: 700; line-height: 24px; }
  .person-title { font-size: 13px; }

  /* Back */
  .card-back {
    background: var(--brand-green);
    color: var(--on-green);
    text-align: center;
    padding-top: 34px;
  }
  .claim { font-size: 17px; font-weight: 600; line-height: 22px; }
  .services { margin-top: 18px; }
  .services-heading { font-size: 15px; font-weight: 600; line-height: 18px; }
  .service-list {
    list-style: none; display: flex; justify-content: center; gap: 12px;
    font-size: 13px; line-height: 18px; margin-bottom: 12px;
  }
  .service-list li::before { content: "\25BE\00a0"; }
  .website {
    position: absolute; left: 0; right: 0; bottom: 30px;
    font-size: 18px; font-weight: 600; letter-spacing: 1px;
  }
</style>
</head>
<body>
<main class="stage">

  <section class="card card-front" aria-label="Business card front">
    <svg class="waves" viewBox="0 0 540 309" preserveAspectRatio="none" aria-hidden="true">
      <path d="M0 212 C170 262 360 236 540 168 L540 309 L0 309 Z" fill="var(--brand-blue-light)"/>
      <path d="M0 220 C170 270 360 244 540 176 L540 290 C360 300 180 300 0 290 Z" fill="var(--brand-blue)"/>
      <path d="M0 290 C180 300 360 300 540 290 L540 309 L0 309 Z" fill="var(--card-white)"/>
      <path d="M0 203 C170 252 360 226 540 158" fill="none" stroke="var(--brand-green)" stroke-width="4"/>
    </svg>

    <div class="brand">
      <span class="brand-dot"></span>
      <span class="brand-name">Brightfold</span>
    </div>

    <ul class="contact">
      <li>
        <svg viewBox="0 0 16 16"><circle cx="8" cy="8" r="8" fill="var(--brand-green)"/><path d="M5 4h2l1 2.5-1.2.8a5 5 0 0 0 2 2l.8-1.2L12 9v2c-4 .5-7.5-3-7-7z" fill="#fff"/></svg>
        (313) 562-9051
      </li>
      <li>
        <svg viewBox="0 0 16 16"><circle cx="8" cy="8" r="8" fill="var(--brand-green)"/><rect x="5.5" y="3.5" width="5" height="9" rx="1" fill="#fff"/></svg>
        (417) 803-2765
      </li>
      <li>
        <svg viewBox="0 0 16 16"><circle cx="8" cy="8" r="8" fill="var(--brand-green)"/><rect x="4" y="5" width="8" height="6" fill="#fff"/><path d="M4 5l4 3 4-3" fill="none" stroke="var(--brand-green)" stroke-width="1"/></svg>
        info@brightfold.com
      </li>
      <li>
        <svg viewBox="0 0 16 16"><circle cx="8" cy="8" r="8" fill="var(--brand-green)"/><circle cx="8" cy="8" r="4" fill="none" stroke="#fff" stroke-width="1.2"/><path d="M4 8h8M8 4v8" stroke="#fff" stroke-width="1"/></svg>
        www.brightfold.com
      </li>
      <li class="address">1879 Marigold, Dunmore MI 48276</li>
    </ul>

    <div class="person">
      <p class="person-name">Your Name</p>
      <p class="person-title">Title</p>
    </div>
  </section>

  <section class="card card-back" aria-label="Business card back">
    <p class="claim">Service Provider For Over 26 Years</p>
    <p class="claim">Top 100 Snow Companies in the U.S.</p>

    <div class="services">
      <p class="services-heading">Winter Services</p>
      <ul class="service-list">
        <li>Snow Plowing</li>
        <li>Sidewalk Cleaning</li>
      </ul>
      <p class="services-heading">Summer Services</p>
      <ul class="service-list">
        <li>Mowing</li>
        <li>Landscaping</li>
        <li>Sodding</li>
        <li>Shrub Trimming</li>
        <li>Clean-ups</li>
      </ul>
    </div>

    <p class="website">www.brightfold.com</p>
  </section>

</main>
</body>
</html>
```